Banner Ad Design Project

Hello,

I need 2 banner designs for advertising on zarvio promoline. Each design must be declined in the following format :

- 300 x 50 Leaderboard pour mobiles
- 468 x 60 Bannière
- 728 x 90 Leaderboard
- 250 x 250 Carré
- 200 x 200 Petit carré
- 336 x 280 Grand rectangle
- 300 x 250 Rectangle intégré
- 120 x 600 Skyscraper
- 160 x 600 Skyscraper large

The banners are to promote an "home exchange" site : http://www.nestrotate.example

Here are the 2 texts that must appear on the banners:
- Say "bye bye" to hotel bill! Stay for free with NestRotate!
- Travel worldwide for free with NestRotate!

Target Market(s)

English customer world wide

Industry/Entity Type

Advertising

Requirements
Must have
• The name "NestRotate" must appear on each banner
The banner must have a look and feel similar of the website http://www.nestrotate.example

```html
<!DOCTYPE html>
<html lang="en">
<head>
<meta charset="utf-8">
<title>NestRotate banner set</title>
<link href="https://fonts.googleapis.com/css2?family=Arimo:wght@400;700&display=swap" rel="stylesheet">
<style>
  :root {
    --blue: #3f78c4;
    --blue-dark: #2a4f95;
    --blue-light: #5b9bd5;
    --green: #2fb31f;
    --green-dark: #1d5e14;
    --lime: #a6dc4c;
    --lime-pale: #c9ec8e;
    --text-green: #3ee41d;
    --red: #e81212;
    --red-bright: #ff2a2a;
    --white: #ffffff;
    --navy: #1f4e9a;
    --photo-room: #b07a4e;
    --photo-stone: #7c7f86;
  }
  * { margin: 0; padding: 0; box-sizing: border-box; }
  html, body { width: 1200px; height: 1200px; overflow: hidden; background: var(--white); }
  .stage {
    position: relative; width: 1000px; height: 1000px;
    transform: scale(1.2); transform-origin: 0 0;
    font-family: "Arimo", Arial, sans-serif; font-weight: 700; color: var(--white);
  }
  .banner { position: absolute; overflow: hidden; background: var(--blue); }
  .abs { position: absolute; }
  .center { text-align: center; }
  .shadow { text-shadow: 1px 1px 1px rgba(0,0,0,.45); }
  .g { color: var(--text-green); }
  .r { color: var(--red); }
  .r-on-blue { color: var(--red-bright); text-shadow: 1px 1px 0 rgba(0,0,0,.55); }
  .photo-room { background: linear-gradient(135deg, #d9a872, var(--photo-room) 55%, #5a3320); }
  .photo-house { background: linear-gradient(160deg, #a9b4c2, var(--photo-stone) 60%, #4c4f55); }
  .photo-person { background: linear-gradient(180deg, #c9d8e4, #b87a5a 45%, #2b2b2b); }
  .icon-house { background: radial-gradient(circle at 50% 55%, #f3f3f3 40%, #d23a2a 41%, #c73224 60%, transparent 61%); }

  /* 468 x 60 */
  .b468 { left: 14px; top: 7px; width: 468px; height: 60px; background: var(--lime); }
  .b468 .photo { left: 0; top: 0; width: 78px; height: 40px; }
  .b468 .tag { left: 80px; top: 2px; width: 84px; height: 36px; background: var(--red); font-size: 12px; padding: 4px; line-height: 14px; }
  .b468 .head { left: 168px; top: 4px; width: 296px; font-size: 12px; line-height: 16px; }
  .b468 .strip { left: 0; top: 40px; width: 468px; height: 20px; background: var(--green-dark); font-size: 13px; font-style: italic; line-height: 20px; padding-left: 98px; }
  .b468 .strip .g { font-size: 15px; }

  /* 300 x 50 */
  .b300 { left: 552px; top: 13px; width: 300px; height: 50px; background: linear-gradient(180deg, #4a86d0, var(--blue-dark)); }
  .b300 .copy { left: 10px; top: 1px; width: 200px; font-size: 10px; line-height: 11px; }
  .b300 .copy .r-on-blue { font-size: 12px; }
  .b300 .side { left: 205px; top: 0; width: 95px; height: 50px; background: linear-gradient(180deg, var(--lime-pale), var(--green)); }
  .b300 .side .house { left: 30px; top: 2px; width: 32px; height: 30px; }
  .b300 .side .name { left: 0; top: 34px; width: 95px; font-size: 11px; }

  /* 728 x 90 */
  .b728 { left: 14px; top: 110px; width: 728px; height: 90px; background: linear-gradient(180deg, #4f8ad6, var(--blue-dark)); }
  .b728 .name { left: 4px; top: 2px; font-size: 16px; }
  .b728 .mascot { left: 4px; top: 24px; width: 66px; height: 66px; }
  .b728 .head { left: 170px; top: 10px; width: 400px; font-size: 15px; line-height: 26px; }
  .b728 .head .big { font-size: 20px; }
  .b728 .more { left: 565px; top: 14px; width: 155px; height: 44px; background: linear-gradient(180deg, var(--lime-pale), var(--lime)); border-radius: 4px; transform: rotate(-3deg); font-size: 30px; line-height: 44px; color: var(--red); }
  .b728 .strip { left: 0; top: 68px; width: 728px; height: 22px; background: var(--green-dark); font-size: 15px; line-height: 22px; padding-left: 170px; color: var(--text-green); }

  /* 200 x 200 */
  .b200 { left: 762px; top: 89px; width: 200px; height: 200px; }
  .b200 .top { left: 0; top: 0; width: 200px; height: 32px; background: linear-gradient(180deg, var(--lime), var(--green)); font-size: 19px; line-height: 32px; }
  .b200 .copy { left: 0; top: 54px; width: 200px; font-size: 13px; line-height: 24px; }
  .b200 .pill { background: var(--red); padding: 0 4px; border: 1px solid var(--white); font-size: 11px; }
  .b200 .travel { left: 0; top: 128px; width: 200px; font-size: 13px; line-height: 20px; color: var(--text-green); }
  .b200 .foot { left: 0; top: 176px; width: 200px; height: 24px; background: var(--green-dark); font-size: 15px; line-height: 26px; }

  /* 336 x 280 */
  .b336 { left: 14px; top: 241px; width: 336px; height: 280px; background: var(--blue-light); border-top: 8px solid var(--blue); }
  .b336 .l1 { left: 0; top: 14px; width: 336px; font-size: 25px; color: var(--text-green); }
  .b336 .l2 { left: 0; top: 56px; width: 336px; font-size: 25px; line-height: 32px; color: var(--text-green); }
  .b336 .l2 .r { font-size: 32px; }
  .b336 .l3 { left: 0; top: 148px; width: 336px; font-size: 20px; }
  .b336 .l4 { left: 0; top: 182px; width: 336px; font-size: 24px; color: var(--text-green); }
  .b336 .base { left: 0; top: 220px; width: 336px; height: 60px; }
  .b336 .base-name { left: 0; top: 230px; width: 336px; font-size: 33px; color: var(--navy); }

  /* 300 x 250 */
  .b300r { left: 360px; top: 243px; width: 300px; height: 250px; background: var(--blue-dark); }
  .b300r .sweep { left: 0; top: 0; }
  .b300r .name { left: 4px; top: 2px; font-size: 22px; }
  .b300r .photo { left: 0; top: 34px; width: 112px; height: 66px; }
  .b300r .l1 { left: 110px; top: 70px; font-size: 12px; }
  .b300r .l1 .g { font-size: 18px; }
  .b300r .l2 { left: 68px; top: 117px; font-size: 13px; }
  .b300r .l2 .r-on-blue { font-size: 15px; }
  .b300r .box { left: 48px; top: 157px; width: 250px; height: 30px; background: #4a7fc8; border: 1px solid #8fb3e4; font-size: 16px; line-height: 28px; }
  .b300r .box .g { font-size: 22px; }
  .b300r .l3 { left: 34px; top: 208px; font-size: 22px; }

  /* 250 x 250 */
  .b250 { left: 396px; top: 525px; width: 250px; height: 250px; background: var(--blue); }
  .b250 .top { left: 0; top: 0; width: 250px; height: 44px; background: linear-gradient(180deg, var(--lime-pale), #7bb25a); font-size: 25px; line-height: 42px; }
  .b250 .cloud { left: 55px; top: 50px; width: 70px; height: 48px; border-radius: 50%; background: radial-gradient(circle, #c7ccd4, #f2f2f2 70%); }
  .b250 .l1 { left: 8px; top: 110px; font-size: 17px; }
  .b250 .l1 .r-on-blue { font-size: 20px; }
  .b250 .l2 { left: 8px; top: 136px; font-size: 16px; }
  .b250 .l3 { left: 8px; top: 156px; font-size: 21px; }
  .b250 .base { left: 0; top: 196px; }
  .b250 .f1 { left: 0; top: 200px; width: 250px; font-size: 15px; }
  .b250 .f1 .r { font-size: 19px; }
  .b250 .f2 { left: 0; top: 224px; width: 250px; font-size: 19px; }

  /* 120 x 600 */
  .b120 { left: 674px; top: 306px; width: 120px; height: 600px; background: linear-gradient(180deg, var(--blue-dark), var(--blue)); }
  .b120 .top { left: 0; top: 0; width: 120px; height: 75px; background: var(--green); font-size: 22px; line-height: 30px; padding-top: 6px; }
  .b120 .photo { left: 0; top: 75px; width: 120px; height: 198px; }
  .b120 .rule { left: 0; top: 273px; width: 120px; height: 6px; background: var(--green-dark); }
  .b120 .t { left: 0; width: 120px; }
  .b120 .star { left: 22px; top: 388px; }
  .b120 .foot { left: 0; top: 565px; width: 120px; height: 35px; background: linear-gradient(180deg, var(--lime-pale), var(--lime)); font-size: 30px; line-height: 36px; color: var(--red); }

  /* 160 x 600 */
  .b160 { left: 808px; top: 304px; width: 160px; height: 600px; background: linear-gradient(180deg, var(--blue-dark), var(--blue)); border-top: 3px solid var(--green-dark); }
  .b160 .top { left: 0; top: 0; width: 160px; height: 62px; background: linear-gradient(180deg, #ffffff, #b9d7a6); font-size: 25px; line-height: 60px; color: var(--green); }
  .b160 .photo { left: 0; top: 62px; width: 160px; height: 113px; }
  .b160 .t { left: 0; width: 160px; }
  .b160 .arrow { left: 4px; top: 305px; }
</style>
</head>
<body>
<div class="stage">

  <section class="banner b468">
    <div class="abs photo photo-room" role="img" aria-label="Photo of a hotel bedroom"></div>
    <div class="abs tag">NestRotate</div>
    <p class="abs head shadow">Say "bye bye" to hotel bill! Stay for free with NestRotate!</p>
    <p class="abs strip">Travel worldwide for free with <span class="g">NestRotate!</span></p>
  </section>

  <section class="banner b300">
    <p class="abs copy">Say <span class="g">"bye bye"</span> to hotel bill!<br>Travel worldwide for <span class="g">free</span> with<br>NestRotate!<br>Stay for <span class="r-on-blue">free</span> with NestRotate!</p>
    <div class="abs side">
      <div class="abs house icon-house" role="img" aria-label="Small house illustration"></div>
      <p class="abs name center">NestRotate</p>
    </div>
  </section>

  <section class="banner b728">
    <p class="abs name">NestRotate</p>
    <div class="abs mascot icon-house" role="img" aria-label="Cartoon house character"></div>
    <p class="abs head center shadow"><span class="g">Say "bye bye" to hotel bill! Stay for free with</span><br><span class="big">NestRotate!</span></p>
    <div class="abs more center">More Info</div>
    <p class="abs strip">Travel worldwide for <span class="r">free</span> with NestRotate!</p>
  </section>

  <section class="banner b200">
    <p class="abs top center shadow">NestRotate!</p>
    <p class="abs copy center">Say "bye bye" to hotel bill!<br>Stay for <span class="pill">free</span> with<br>NestRotate!</p>
    <p class="abs travel center shadow">Travel! <span style="color:var(--white)">worldwide</span> for<br>free with NestRotate!</p>
    <p class="abs foot center">Click More info</p>
  </section>

  <section class="banner b336">
    <p class="abs l1 center shadow">Say "bye bye" to hotel bill!</p>
    <p class="abs l2 center shadow">Stay for <span class="r">free</span> with<br>NestRotate!</p>
    <p class="abs l3 center">Travel worldwide for free with</p>
    <p class="abs l4 center shadow">NestRotate!</p>
    <svg class="abs base" width="336" height="60" viewBox="0 0 336 60"><path d="M0 8 Q168 -6 336 8 V60 H0Z" fill="var(--lime)"/><path d="M0 8 Q168 -6 336 8" stroke="var(--green)" stroke-width="3" fill="none"/></svg>
    <p class="abs base-name center">NestRotate</p>
  </section>

  <section class="banner b300r">
    <svg class="abs sweep" width="300" height="250" viewBox="0 0 300 250"><path d="M0 0 H220 Q130 40 60 250 H0Z" fill="#3a6cb8"/></svg>
    <p class="abs name">nest <span class="g">rotate</span></p>
    <div class="abs photo photo-house" role="img" aria-label="Photo of an old stone house"></div>
    <p class="abs l1">Say "bye bye" to <span class="g">hotel bill!</span></p>
    <p class="abs l2">Stay for <span class="r-on-blue">free</span> with NestRotate!</p>
    <p class="abs box center">Travel worldwide for <span class="g">free</span></p>
    <p class="abs l3">with NestRotate!</p>
  </section>

  <section class="banner b250">
    <p class="abs top center shadow">NestRotate</p>
    <div class="abs cloud" role="img" aria-label="Thought bubble with a house"></div>
    <p class="abs l1">Say "bye bye" to <span class="r-on-blue">hotel bill!</span></p>
    <p class="abs l2">Stay for free with</p>
    <p class="abs l3">NestRotate!</p>
    <svg class="abs base" width="250" height="54" viewBox="0 0 250 54"><path d="M0 6 Q125 -4 250 6 V54 H0Z" fill="var(--green)"/><path d="M0 6 Q125 -4 250 6" stroke="var(--lime-pale)" stroke-width="2" fill="none"/></svg>
    <p class="abs f1 center">Travel worldwide for <span class="r">free</span></p>
    <p class="abs f2 center">with NestRotate!</p>
  </section>

  <section class="banner b120">
    <p class="abs top center">Nest<br><span style="color:var(--navy)">Rotate</span></p>
    <div class="abs photo photo-person" role="img" aria-label="Photo of a woman holding a house key"></div>
    <div class="abs rule"></div>
    <p class="abs t center" style="top:292px;font-size:12px">Say "bye bye" to</p>
    <p class="abs t center shadow" style="top:318px;font-size:22px;color:var(--lime)">hotel bill!</p>
    <p class="abs t center" style="top:354px;font-size:21px">Stay for</p>
    <svg class="abs star" width="76" height="76" viewBox="0 0 76 76"><polygon fill="var(--red)" points="38,0 44,12 56,4 57,18 71,16 66,29 76,38 66,47 71,60 57,58 56,72 44,64 38,76 32,64 20,72 19,58 5,60 10,47 0,38 10,29 5,16 19,18 20,4 32,12"/><text x="38" y="45" text-anchor="middle" font-family="Arimo, sans-serif" font-weight="700" font-size="22" fill="var(--text-green)">free</text></svg>
    <p class="abs t center" style="top:470px;font-size:21px;line-height:28px">with<br>Nest<br><span class="g">Rotate!</span></p>
    <p class="abs foot center">Click</p>
  </section>

  <section class="banner b160">
    <p class="abs top center">NestRotate</p>
    <div class="abs photo photo-room" role="img" aria-label="Photo of a hotel bedroom"></div>
    <p class="abs t center" style="top:186px;font-size:20px;line-height:24px">Say "bye bye"<br>to</p>
    <p class="abs t center shadow" style="top:234px;font-size:32px;color:var(--text-green)">hotel bill!</p>
    <p class="abs t center" style="top:278px;font-size:22px">Stay for</p>
    <svg class="abs arrow" width="154" height="56" viewBox="0 0 154 56"><defs><linearGradient id="arrowFill" x1="0" y1="0" x2="0" y2="1"><stop offset="0" stop-color="#7fd4f2"/><stop offset="1" stop-color="#1c86c8"/></linearGradient></defs><polygon points="0,14 112,14 112,0 154,28 112,56 112,42 0,42" fill="url(#arrowFill)"/><text x="72" y="38" text-anchor="middle" font-family="Arimo, sans-serif" font-weight="700" font-size="30" fill="var(--red)">free</text></svg>
    <p class="abs t center" style="top:360px;font-size:20px;line-height:31px">with<br>NestRotate!</p>
    <p class="abs t center" style="top:428px;font-size:17px;line-height:29px">Travel worldwide<br>for</p>
    <p class="abs t center" style="top:480px;font-size:26px;color:var(--text-green)">free</p>
    <p class="abs t center" style="top:512px;font-size:20px;line-height:25px">with<br>Nest<br><span class="g" style="font-size:22px">Rotate!</span></p>
  </section>

</div>
</body>
</html>
```